Quillbrook IT company focused on 3 areas of IT

Looking for something similar to attached cards. Logo for quillbrook also attached.. Looking for something clean as far as colors (surprise me).. 3 tech stands for 3 primary areas, web design, consulting and network infrastructure design. Please email me if you have any questions. Looking forward to seeing how creative and professional this card will look. Thank you,

Target Market(s)

Small business/consumers looking for It services

Industry/Entity Type

It Service

Contact Information for Business Card

Darvin Pell
Principal Consultant

202-555-0173

www.quillbrook-example.com
dpell@quillbrook-example.com

46210 Marsh Lantern Ct,
Fernhollow, OR 97999

Colors

Designer to choose colors to be used in the design.

Requirements
Must have
• attached Logo design. Feel free to play with the colors.. If you have a better idea for a card, please fee free to send me. Looking for something clean/modern. Should have tech feel, not cheesy.
Nice to have
• Surprise me :-)..

```html
<!DOCTYPE html>
<html lang="en">
<head>
<meta charset="utf-8">
<title>Quillbrook Business Card</title>
<link href="https://fonts.googleapis.com/css2?family=Lato:wght@300;400;700;900&display=swap" rel="stylesheet">
<style>
  :root {
    --backdrop: #262829;
    --card-dark: #1d2a2d;
    --band-dark: #1f2c2f;
    --band-light: #2e434a;
    --ink: #ffffff;
    --ink-soft: #d9e2e4;
  }
  * { box-sizing: border-box; margin: 0; padding: 0; }
  html, body {
    width: 1200px; height: 900px; overflow: hidden;
    background: var(--backdrop);
    font-family: "Lato", sans-serif;
    color: var(--ink);
  }
  .stage {
    width: 1200px; height: 900px;
    display: flex; align-items: center; justify-content: center; gap: 70px;
  }
  .card {
    border-radius: 14px;
    overflow: hidden;
    box-shadow: 0 14px 30px rgba(0,0,0,0.45);
  }
  /* Front */
  .card-front {
    width: 580px; height: 330px;
    background: var(--card-dark);
    display: flex; flex-direction: column; align-items: center; justify-content: center;
  }
  .brand {
    display: flex; align-items: center; gap: 14px;
    font-weight: 900; font-size: 44px; letter-spacing: 2px; text-transform: uppercase;
  }
  .brand-square { width: 26px; height: 26px; background: var(--ink); }
  .website {
    margin-top: 56px;
    font-weight: 700; font-size: 15px; letter-spacing: 4px;
  }
  /* Back */
  .card-back {
    width: 330px; height: 580px;
    display: flex; flex-direction: column;
  }
  .band {
    position: relative;
    display: flex; align-items: center; gap: 16px;
    padding: 0 22px 0 26px;
  }
  .band-name {
    height: 160px; background: var(--band-dark);
    flex-direction: column; align-items: flex-start; justify-content: center; gap: 6px;
    padding-left: 30px;
    z-index: 2;
  }
  .band-name::after {
    content: ""; position: absolute; right: 70px; bottom: -18px;
    border-left: 22px solid transparent; border-right: 22px solid transparent;
    border-top: 18px solid var(--band-dark);
  }
  .person-name { font-size: 34px; letter-spacing: 1px; text-transform: uppercase; font-weight: 400; }
  .person-name .first { font-weight: 900; }
  .person-name .last { font-weight: 300; }
  .person-role { font-weight: 300; font-size: 16px; color: var(--ink-soft); }
  .band-phone { height: 130px; background: var(--band-light); }
  .band-email { height: 130px; background: var(--band-dark); }
  .band-address { height: 160px; background: var(--band-light); }
  .icon { width: 40px; height: 40px; flex: none; }
  .detail { font-weight: 700; font-size: 15px; line-height: 1.4; white-space: nowrap; }
  .detail-email { font-size: 14px; }
  .detail-phone { font-size: 20px; letter-spacing: 0.5px; }
</style>
</head>
<body>
<main class="stage">
  <section class="card card-front">
    <div class="brand"><span class="brand-square"></span><span>Quillbrook</span></div>
    <p class="website">www.quillbrook-example.com</p>
  </section>

  <section class="card card-back">
    <div class="band band-name">
      <h1 class="person-name"><span class="first">Darvin</span> <span class="last">Pell</span></h1>
      <p class="person-role">Principal Consultant</p>
    </div>
    <div class="band band-phone">
      <svg class="icon" viewBox="0 0 48 48" aria-hidden="true">
        <path d="M4 16c0-6 8-9 20-9s20 3 20 9v3h-9v-4c-3-1-7-1.5-11-1.5S16 14 13 15v4H4z" fill="#fff"/>
        <path d="M10 22h28l4 18H6z" fill="#fff"/>
        <g fill="#2e434a">
          <rect x="17" y="25" width="4" height="3"/><rect x="22" y="25" width="4" height="3"/><rect x="27" y="25" width="4" height="3"/>
          <rect x="16" y="30" width="4" height="3"/><rect x="22" y="30" width="4" height="3"/><rect x="28" y="30" width="4" height="3"/>
          <rect x="15" y="35" width="4" height="3"/><rect x="22" y="35" width="4" height="3"/><rect x="29" y="35" width="4" height="3"/>
        </g>
      </svg>
      <p class="detail detail-phone">202-555-0173</p>
    </div>
    <div class="band band-email">
      <svg class="icon" viewBox="0 0 48 48" aria-hidden="true">
        <rect x="4" y="10" width="40" height="28" rx="3" fill="#fff"/>
        <path d="M6 13l18 14 18-14M6 36l14-12M42 36L28 24" stroke="#1f2c2f" stroke-width="2.5" fill="none"/>
      </svg>
      <p class="detail detail-email">dpell@quillbrook-example.com</p>
    </div>
    <div class="band band-address">
      <svg class="icon" viewBox="0 0 48 48" aria-hidden="true">
        <path d="M24 6L4 22h7v18h10V30h6v10h10V22h7z" fill="#fff"/>
      </svg>
      <p class="detail">46210 Marsh Lantern Ct,<br>Fernhollow, OR 97999</p>
    </div>
  </section>
</main>
</body>
</html>
```